Modern Business Card for Industrial Company

We need business cards updated with modern fonts and make it look more technical, sharp and clean. The logo should not be changed, but we are looking for fresh solutions for how other information on the card is laid out in an interesting way. The company provides machinery and services to the ceramic industry and deals with cutting-edge technology. The design should reflect a technologically advanced and modern company that deals with the latest European technologies.

Font styles to use
Sans Serif

Requirements
Must have
• Modern fonts, technical look and feel

```html
<!DOCTYPE html>
<html lang="en">
<head>
<meta charset="utf-8">
<title>Novatec Service – Business Card</title>
<link rel="stylesheet" href="https://fonts.googleapis.com/css2?family=Exo+2:wght@500;800&family=Rajdhani:wght@500&display=swap">
<style>
  :root {
    --brand-blue: #02528c;
    --steel-grey: #9a9da3;
    --light-grey: #e4e6ea;
    --text-grey: #8e9198;
    --paper: #ffffff;
  }
  * { margin: 0; padding: 0; box-sizing: border-box; }
  html, body { width: 1200px; height: 960px; overflow: hidden; background: var(--paper); }
  .canvas { position: relative; width: 1200px; height: 960px; }

  /* Front */
  .card-front {
    position: absolute; left: 95px; top: 59px; width: 687px; height: 393px;
    background: var(--brand-blue); color: var(--paper);
  }
  .front-wordmark {
    position: absolute; left: 190px; top: 70px; width: 307px;
    font-family: "Exo 2", sans-serif; font-weight: 800; text-align: center; line-height: 1;
  }
  .front-wordmark .name { display: block; font-size: 74px; letter-spacing: 1px; }
  .front-wordmark .sub { display: block; font-size: 44px; letter-spacing: 6px; margin-top: 22px; padding-left: 6px; }
  .front-rule { position: absolute; left: 191px; top: 307px; width: 307px; height: 2px; background: var(--paper); }
  .front-url {
    position: absolute; left: 191px; top: 315px; width: 307px;
    font-family: "Exo 2", sans-serif; font-weight: 500; font-size: 12.5px;
    letter-spacing: 6.1px; text-align: center; white-space: nowrap;
  }

  /* Back */
  .card-back {
    position: absolute; left: 416px; top: 506px; width: 689px; height: 394px;
    border: 2px solid var(--steel-grey); background: var(--paper); overflow: hidden;
  }
  .card-back .graphics { position: absolute; left: -2px; top: -2px; width: 689px; height: 394px; }
  .holder { position: absolute; right: 103px; top: 49px; text-align: right; }
  .holder-name {
    font-family: "Exo 2", sans-serif; font-weight: 500; font-size: 27px;
    color: var(--brand-blue); line-height: 1; letter-spacing: -0.3px;
  }
  .holder-title {
    display: flex; align-items: center; gap: 10px; margin-top: 5px;
    font-family: "Rajdhani", sans-serif; font-weight: 500; font-size: 14px;
    color: var(--text-grey); letter-spacing: 4.3px; line-height: 1;
  }
  .holder-title::before { content: ""; width: 108px; height: 1.5px; background: var(--text-grey); }
  .contact {
    position: absolute; left: 38px; top: 262px; list-style: none;
    font-family: "Rajdhani", sans-serif; font-weight: 500; font-size: 20px;
    color: var(--text-grey); line-height: 24px; text-transform: uppercase;
  }
  .contact li { display: flex; align-items: flex-start; }
  .contact .icon { width: 16px; height: 24px; margin-right: 5px; flex: none; }
  .contact .indent { padding-left: 21px; }
  .back-wordmark {
    position: absolute; left: 450px; top: 232px; width: 190px; text-align: center;
    font-family: "Exo 2", sans-serif; font-weight: 800; color: var(--brand-blue); line-height: 1;
  }
  .back-wordmark .name { display: block; font-size: 44px; }
  .back-wordmark .sub { display: block; font-size: 27px; letter-spacing: 3px; margin-top: 14px; padding-left: 3px; }
</style>
</head>
<body>
<main class="canvas">

  <section class="card-front" aria-label="Card front">
    <div class="front-wordmark"><span class="name">NOVATEC</span><span class="sub">SERVICE</span></div>
    <div class="front-rule"></div>
    <p class="front-url">WWW.NOVATECSERVICE.COM</p>
  </section>

  <section class="card-back" aria-label="Card back">
    <svg class="graphics" viewBox="0 0 689 394" aria-hidden="true">
      <!-- top header band -->
      <rect x="0" y="0" width="689" height="10" fill="var(--brand-blue)"/>
      <rect x="0" y="10" width="240" height="4" fill="var(--steel-grey)"/>
      <!-- divider under header -->
      <rect x="0" y="150" width="689" height="22" fill="var(--light-grey)"/>
      <rect x="0" y="150" width="300" height="22" fill="var(--steel-grey)"/>
      <rect x="300" y="158" width="389" height="6" fill="var(--brand-blue)"/>
      <!-- vertical divider between contact and brand -->
      <line x1="420" y1="210" x2="420" y2="362" stroke="var(--steel-grey)" stroke-width="1.5"/>
      <!-- small markers -->
      <rect x="38" y="210" width="10" height="10" fill="var(--brand-blue)"/>
      <rect x="54" y="210" width="10" height="10" fill="var(--steel-grey)"/>
      <rect x="70" y="210" width="10" height="10" fill="var(--light-grey)"/>
      <!-- bottom strip -->
      <rect x="0" y="384" width="689" height="10" fill="var(--steel-grey)"/>
      <rect x="449" y="384" width="240" height="10" fill="var(--brand-blue)"/>
    </svg>

    <div class="holder">
      <p class="holder-name">MARCO BELLINI</p>
      <p class="holder-title">PRESIDENT</p>
    </div>

    <ul class="contact">
      <li>
        <svg class="icon" viewBox="0 0 16 24" aria-hidden="true"><path d="M8 6a4 4 0 0 1 4 4c0 3-4 7-4 7s-4-4-4-7a4 4 0 0 1 4-4z" fill="var(--brand-blue)"/><circle cx="8" cy="10" r="1.5" fill="#fff"/></svg>
        418 Kepler Road, Suite 200
      </li>
      <li class="indent">Northfield, GA 30099</li>
      <li>
        <svg class="icon" viewBox="0 0 16 24" aria-hidden="true"><rect x="1.5" y="8" width="13" height="9" fill="none" stroke="var(--brand-blue)" stroke-width="1.5"/><polyline points="1.5,8 8,13 14.5,8" fill="none" stroke="var(--brand-blue)" stroke-width="1.5"/></svg>
        mbellini@novatecservice.com
      </li>
      <li>
        <svg class="icon" viewBox="0 0 16 24" aria-hidden="true"><path d="M9 8c-3 1-3 8 0 9l1-2c-1.5-.8-1.5-4.2 0-5z" fill="var(--brand-blue)"/></svg>
        555 010-4827
      </li>
    </ul>

    <div class="back-wordmark"><span class="name">NOVATEC</span><span class="sub">SERVICE</span></div>
  </section>

</main>
</body>
</html>
```